Hello my Name is Esteban Ortiz. I buy and sell vintage comic books, you can refer to my instragram page qrkp.comics to get ideas and inspiration. For the front of the card I would like my company logo QRKP Comics with a yellow and black background with the bat signal or bat emblem like on my IG page and with my info Esteban Ortiz as the Owner and address/ phone number, PO Box 218873, Miami, FL 33144, 305-555-0182 and that I buy and sell comics & collectables . Also feel free to be open to other ideas if you want. Im not stuck on one design. For the back of the card I would like for it to say follow me on Instagram QRKP.Comics with the ig emblem. Also would like the card to be vertical if possible. Thanks

```html
<!DOCTYPE html>
<html lang="en">
<head>
<meta charset="utf-8">
<title>QRKP Comics – Business Card</title>
<link rel="stylesheet" href="https://fonts.googleapis.com/css2?family=Exo+2:wght@700;800&family=Open+Sans:wght@400;600&display=swap">
<style>
  :root {
    --yellow: #fcc419;
    --yellow-deep: #f2b000;
    --black: #111111;
    --stage: #1d1d1d;
  }
  * { box-sizing: border-box; margin: 0; padding: 0; }
  html, body {
    width: 1200px; height: 852px; overflow: hidden;
    background: var(--stage);
  }
  .stage {
    position: relative; width: 1200px; height: 852px;
    display: flex; justify-content: center; align-items: center; gap: 80px;
  }
  .card {
    position: relative; width: 380px; height: 660px;
    background: var(--yellow);
    overflow: hidden;
    font-family: "Open Sans", sans-serif;
    color: var(--black);
  }
  .brand {
    position: absolute; left: 0; right: 0;
    display: flex; align-items: center; justify-content: center; gap: 14px;
  }
  .brand-dot {
    width: 46px; height: 46px; border-radius: 50%;
    background: var(--black); flex: none;
  }
  .brand-name {
    font-family: "Exo 2", sans-serif; font-weight: 800;
    font-size: 40px; letter-spacing: 1px; color: var(--black);
    white-space: nowrap;
  }
  .card--back .brand { top: 300px; }
  .card--back .website {
    position: absolute; left: 0; right: 0; bottom: 48px;
    text-align: center;
    font-family: "Exo 2", sans-serif; font-weight: 800; font-size: 22px;
  }
  .card--front .brand { top: 92px; }
  .details {
    position: absolute; top: 200px; left: 0; right: 0; text-align: center;
  }
  .details .name {
    font-family: "Exo 2", sans-serif; font-weight: 800; font-size: 27px;
    letter-spacing: 1px; text-transform: uppercase;
  }
  .details .role {
    font-family: "Exo 2", sans-serif; font-weight: 700; font-size: 18px;
    text-transform: uppercase; margin-bottom: 14px;
  }
  .details .line { font-size: 16px; line-height: 1.45; }
  .edge-area {
    position: absolute; left: 0; top: 430px; width: 380px; height: 110px;
    background: linear-gradient(to bottom, var(--yellow) 0%, var(--yellow-deep) 100%);
  }
  .bottom-band {
    position: absolute; left: 0; bottom: 0; width: 380px; height: 120px;
    background: var(--black);
  }
  .tagline {
    position: absolute; left: 0; right: 0; bottom: 26px; text-align: center;
    font-family: "Exo 2", sans-serif; font-weight: 800; font-size: 17px;
    color: var(--yellow); text-transform: uppercase; letter-spacing: 0.5px;
    white-space: nowrap;
  }
</style>
</head>
<body>
<main class="stage">
  <section class="card card--back">
    <div class="brand">
      <span class="brand-dot"></span>
      <span class="brand-name">QRKP Comics</span>
    </div>
    <p class="website">www.qrkpcomics.com</p>
  </section>

  <section class="card card--front">
    <div class="brand">
      <span class="brand-dot"></span>
      <span class="brand-name">QRKP Comics</span>
    </div>
    <div class="details">
      <p class="name">Esteban Ortiz</p>
      <p class="role">Owner</p>
      <p class="line">PO Box 218873, Miami, FL 33144</p>
      <p class="line">305-555-0182</p>
      <p class="line">www.qrkpcomics.com</p>
      <p class="line">Instragram: qrkp.comics</p>
    </div>
    <div class="edge-area" role="img" aria-label="Decorative edge graphic area above the black band"></div>
    <div class="bottom-band"></div>
    <p class="tagline">Buy and sell comics &amp; collectables</p>
  </section>
</main>
</body>
</html>
```